Book Cover for my Autobiography

I would like to see a CONCEPT of the Front Cover as per the following.
a) Take me out of the FILE NAMED=1-MAIN.jpg
b) I want my Wife "Watching over me" - behind me - in the SHADOWS. You can take her image for the concept from the FILE NAMED=2-Wife Watching over me.jpg.
c) This based on the old saying that "Behind every Good Man....is a Woman".  So that's what I want to convert because my wife has always been in the background, in the "Shadows" - always supporting and encouraging me in whatever I do.
d) This book is purely for my children, wife, siblings, relatives and Friends.
e) the Book Cover has to be designed FLAT & RECTANGULAR - like the sample leather cover.  i.e. NOT viewed from an Angle.
f) The Book Title is "Salt in the Orchard"
g) I have no pre-conceived ideas of design or colours or styling etc.  I want a PROFESSIONAL DESIGNER to come up with the best Overall Design that conveys the "Supportive Wife" always behind me and supporting me - While I am out front as the subject.
h) When the Design is accepted, I will provide the main photo of my wife without my son in front of her that I want to use - and one me without my wife's arms around me.  But if you can do that too (i.e. reconstruct my Wife's Burgundy top & and remove her arms from around me-then even better because I don't have to hire another graphic designer to do that for me).
My name is "Tomas Brenhoek" so the author of the autobiography needs to be SOMEWHERE.
h) And last, please just put some text - maybe 2 sentences for the summary of the story like many Autobiographies do. eg.
"My story of how ....Lorem ipsum dolor sit amet, consectetur adipiscing elit, sed do eiusmod tempor incididunt. Integer vitae justo eget magna fermentum iaculis eu non. Aliquam eleifend".

I forgot to mention that this Book Cover is actually going on an eBOOK - not a Printed Book.
It's just for Family and Friends.

```html
<!DOCTYPE html>
<html lang="en">
<head>
<meta charset="utf-8">
<title>Salt in the Orchard — Book Cover</title>
<link href="https://fonts.googleapis.com/css2?family=Saira:ital,wght@0,700;0,800;0,900;1,700&display=swap" rel="stylesheet">
<style>
  :root {
    --cover-blue: #3d9bd6;
    --paper: #ffffff;
    --ink-light: #ffffff;
    --photo-navy: #1c2a48;
    --photo-red: #b8322c;
    --photo-skin: #d9a58a;
  }
  html, body {
    margin: 0;
    padding: 0;
    width: 1200px;
    height: 1000px;
    overflow: hidden;
    background: var(--paper);
  }
  .canvas {
    position: relative;
    width: 1200px;
    height: 1000px;
    background: var(--paper);
  }
  .cover {
    position: absolute;
    left: 247px;
    top: 54px;
    width: 705px;
    height: 891px;
    background: var(--cover-blue);
    font-family: "Saira", "Arial Narrow", sans-serif;
    color: var(--ink-light);
  }
  .spine-text {
    position: absolute;
    left: 37px;
    transform-origin: 0 0;
    transform: rotate(90deg);
    white-space: nowrap;
    text-transform: uppercase;
    line-height: 1;
  }
  .spine-author {
    top: 74px;
    left: 48px;
    font-size: 20px;
    font-weight: 800;
    letter-spacing: 3px;
  }
  .spine-title {
    top: 337px;
    left: 60px;
    font-size: 40px;
    font-weight: 900;
    letter-spacing: 1px;
  }
  .title {
    position: absolute;
    left: 75px;
    right: 0;
    top: 28px;
    margin: 0;
    text-align: center;
    font-size: 108px;
    font-weight: 900;
    line-height: 92px;
    text-transform: uppercase;
    letter-spacing: 1px;
  }
  .title span { display: block; }
  .summary {
    position: absolute;
    left: 75px;
    right: 0;
    top: 320px;
    margin: 0;
    text-align: center;
    font-size: 12px;
    font-weight: 700;
    font-style: italic;
    line-height: 15px;
    text-transform: uppercase;
    letter-spacing: 0.4px;
  }
  .photo-panel {
    position: absolute;
    left: 75px;
    top: 383px;
    width: 630px;
    height: 441px;
    background: var(--paper);
    overflow: hidden;
  }
  .portrait {
    position: absolute;
    left: 112px;
    top: 26px;
    width: 457px;
    height: 410px;
    background:
      radial-gradient(ellipse 30% 40% at 70% 38%, var(--photo-skin) 0%, rgba(217,165,138,0) 100%),
      radial-gradient(ellipse 25% 45% at 28% 45%, var(--photo-red) 0%, rgba(184,50,44,0) 100%),
      radial-gradient(ellipse 55% 60% at 60% 55%, var(--photo-navy) 0%, rgba(28,42,72,0.6) 55%, rgba(255,255,255,0) 100%);
  }
  .author {
    position: absolute;
    left: 75px;
    right: 0;
    bottom: 20px;
    margin: 0;
    text-align: center;
    font-size: 22px;
    font-weight: 800;
    letter-spacing: 3px;
    text-transform: uppercase;
  }
</style>
</head>
<body>
  <div class="canvas">
    <div class="cover">
      <div class="spine-text spine-author">Tomas Brenhoek</div>
      <div class="spine-text spine-title">Salt in the Orchard</div>

      <h1 class="title">
        <span>Salt in</span>
        <span>the</span>
        <span>Orchard</span>
      </h1>

      <p class="summary">
        My story of how ....Lorem ipsum dolor sit amet, consectetur<br>
        adipiscing elit, sed do eiusmod tempor incididunt.<br>
        Integer vitae justo eget magna fermentum iaculis eu non. Aliquam eleifend
      </p>

      <div class="photo-panel">
        <div class="portrait" role="img" aria-label="Portrait of the author smiling in the foreground, with his wife watching over him from behind and their young son beside her"></div>
      </div>

      <p class="author">Tomas Brenhoek</p>
    </div>
  </div>
</body>
</html>
```